KEV Holding

KEV holding is located in the UAE. In the company, there are several departments covering Hospitality management, Facility Management, interior design and Construction.

The logo should not include the name holding, Just KEV.

Needed Items:

(1) Logo.
(2) Business Card.
(3) Letterhead
(4) Envelope
(5) cd cover
(6) email signature
Updates

The previous brief was misplaced with another competition. Current update is the final.

Target Market(s)

Collaboration with international high end firms.

Industry/Entity Type

Business

Requirements
Must have
• COLOR PREFERENCE Maximum 2 colors, preferably mono-color with different shades.
Nice to have
• Elegant, luxurious, and minimalistic.

```html
<!DOCTYPE html>
<html lang="en">
<head>
<meta charset="utf-8">
<title>KEV – Business Card</title>
<link href="https://fonts.googleapis.com/css2?family=Montserrat:wght@400;600&family=Arimo:wght@400&display=swap" rel="stylesheet">
<style>
  :root {
    --backdrop: #2a2a2c;
    --brand-blue: #1480d6;
    --brand-blue-deep: #0a5aa8;
    --paper: #f4f5f6;
    --ink: #2b2b2b;
    --rule: #d2d4d6;
    --white: #ffffff;
  }
  * { margin: 0; padding: 0; box-sizing: border-box; }
  html, body { width: 1200px; height: 900px; overflow: hidden; }
  body {
    background: var(--backdrop);
    display: flex;
    flex-direction: column;
    align-items: center;
    justify-content: center;
    gap: 60px;
  }
  .card {
    width: 630px;
    height: 360px;
    position: relative;
  }
  .card--front {
    background: linear-gradient(160deg, var(--brand-blue-deep) 0%, var(--brand-blue) 100%);
    display: flex;
    align-items: center;
    justify-content: center;
  }
  .wordmark {
    font-family: "Montserrat", sans-serif;
    font-weight: 600;
    line-height: 1;
    letter-spacing: 6px;
  }
  .card--front .wordmark { color: var(--white); font-size: 110px; }

  .card--back {
    background: var(--paper);
    display: flex;
  }
  .card__brand {
    width: 275px;
    display: flex;
    align-items: center;
    justify-content: center;
    border-right: 1px solid var(--rule);
    margin: 40px 0;
  }
  .card__brand .wordmark { color: var(--brand-blue); font-size: 72px; letter-spacing: 4px; }

  .card__details {
    padding: 70px 0 0 34px;
    font-family: "Arimo", sans-serif;
    color: var(--ink);
  }
  .person__name {
    font-family: "Montserrat", sans-serif;
    font-weight: 600;
    color: var(--brand-blue);
    font-size: 25px;
    letter-spacing: 0.5px;
  }
  .person__title { font-size: 17px; margin-top: 2px; }
  .contact { list-style: none; margin-top: 14px; }
  .contact li {
    display: flex;
    align-items: center;
    gap: 8px;
    font-size: 17px;
    line-height: 26px;
  }
  .contact svg { width: 15px; height: 15px; fill: var(--brand-blue); flex: none; }
  .contact .accent { color: var(--brand-blue); }
  .address { font-size: 17px; line-height: 23px; margin-top: 14px; padding-left: 23px; }
</style>
</head>
<body>
  <section class="card card--front">
    <div class="wordmark">KEV</div>
  </section>

  <section class="card card--back">
    <div class="card__brand">
      <div class="wordmark">KEV</div>
    </div>
    <div class="card__details">
      <h1 class="person__name">DANIEL MORGAN</h1>
      <p class="person__title">Managing Director</p>
      <ul class="contact">
        <li>
          <svg viewBox="0 0 16 16" aria-hidden="true"><path d="M3.6 1.2l2.3 2.6-1.3 1.6c.9 2 2.6 3.7 4.6 4.7l1.6-1.3 2.7 2.2-1.3 2.4C7.1 13.3 2.5 8.8 1.2 3z"/></svg>
          044-987 654 321
        </li>
        <li>
          <svg viewBox="0 0 16 16" aria-hidden="true"><path d="M1 3h14v10H1z M1.5 3.5L8 9l6.5-5.5" stroke="#f4f5f6" stroke-width="1"/></svg>
          info@kevmail.com
        </li>
        <li>
          <svg viewBox="0 0 16 16" aria-hidden="true"><circle cx="8" cy="8" r="7"/><path d="M1 8h14M8 1c-3 3.5-3 10.5 0 14M8 1c3 3.5 3 10.5 0 14" stroke="#f4f5f6" stroke-width="1" fill="none"/></svg>
          <span>www.<span class="accent">kevholding-site</span>.com</span>
        </li>
      </ul>
      <p class="address">88, Marina Tower Road<br>10231, Dubai UAE</p>
    </div>
  </section>
</body>
</html>
```